'Rebuild' the outer box design of foam cleaner

I have had the bottle label designed as attached. But I chose not to assign this project to the original bottle label designer. Because I don't expect the outer box to be cloned with the label, though they should be in a similar style. I hope you guys to work out an exquisite box for the product with your own marks. Of course, I also don't like the box to be designed totally different with the label too. Under the same design rule of the label, the box should have its own characteristics.

Target Market(s)

16-35 female, orthodontic patients.

Requirements
Must have
• 1.Bar code must show on the outer box. But it could be customized to be other styles.
2.All the contents in the document 'OUTERCONTAINERDESIGN' must be involved. Surely designers could add some other reasonable elements.
Nice to have
• it's nice to have the pic of clear aligner involved.
Should not have
• the QR code on the label should not exist on the outer box.

```html
<!DOCTYPE html>
<html lang="en">
<head>
<meta charset="utf-8">
<title>Bloom Froth Aligner Cleaner – Outer Box</title>
<link rel="stylesheet" href="https://fonts.googleapis.com/css2?family=Josefin+Sans:wght@600;700&family=Poppins:wght@400&family=Marcellus&family=Oswald:wght@400&display=swap">
<style>
  :root {
    --stage: #eceff3;
    --sky-deep: #3b98d8;
    --sky-mid: #8cc3ea;
    --sky-pale: #e6f2fb;
    --paper: #ffffff;
    --ink: #111418;
    --navy: #0b4fae;
    --royal: #1a5fc0;
    --mint: #1de3c4;
    --mint-text: #14c9ad;
    --mist: #dfe4ea;
  }
  * { margin: 0; padding: 0; box-sizing: border-box; }
  html, body { width: 1200px; height: 1200px; overflow: hidden; background: var(--stage); }
  .canvas { position: relative; width: 1200px; height: 1200px; }

  .box-front {
    position: absolute; left: 458px; top: 50px;
    width: 285px; height: 1100px; overflow: hidden;
    background: linear-gradient(180deg, var(--sky-deep) 0%, var(--sky-mid) 28%, var(--sky-pale) 46%, var(--paper) 58%, var(--paper) 100%);
    box-shadow: 0 6px 24px rgba(0,0,0,0.12);
  }
  .soft-curves { position: absolute; inset: 0; width: 100%; height: 100%; }

  .brand-name {
    position: absolute; left: 0; right: 0; top: 168px;
    text-align: center; color: var(--paper);
    font-family: 'Josefin Sans', sans-serif; font-weight: 700;
    font-size: 40px; line-height: 44px; letter-spacing: 1px;
  }
  .brand-dot {
    position: absolute; left: 226px; top: 146px;
    width: 18px; height: 18px; border-radius: 50%;
    border: 3px solid var(--paper);
  }

  .product-title {
    position: absolute; left: 0; right: 0; top: 330px; text-align: center;
    font-family: 'Josefin Sans', sans-serif; font-weight: 600;
  }
  .product-title .line-one { display: block; color: var(--ink); font-size: 34px; letter-spacing: 2px; line-height: 38px; }
  .product-title .line-two { display: block; color: var(--paper); font-size: 40px; letter-spacing: 3px; line-height: 42px; }

  .supply-tag {
    position: absolute; left: 58px; top: 424px; width: 169px; height: 30px;
    background: var(--navy); color: var(--paper);
    font-family: 'Poppins', sans-serif; font-size: 15px; letter-spacing: 1px;
    display: flex; align-items: center; justify-content: center;
  }

  .benefit-list {
    position: absolute; left: 48px; top: 520px; list-style: none;
    font-family: 'Poppins', sans-serif; font-size: 19px; color: var(--royal);
  }
  .benefit-list li { display: flex; align-items: center; height: 30px; }
  .benefit-list svg { width: 14px; height: 14px; margin-right: 10px; flex: none; }

  .flavor-badge {
    position: absolute; left: 122px; top: 683px; width: 44px; height: 44px;
    border-radius: 50%; background: var(--mint);
  }
  .flavor-name {
    position: absolute; left: 0; right: 0; top: 732px; text-align: center;
    font-family: 'Marcellus', serif; font-size: 18px; color: var(--mint-text);
  }

  .aligner-photo {
    position: absolute; left: 10px; right: 0; top: 765px; height: 265px;
    background: radial-gradient(ellipse at 55% 45%, #f4f6f8 0%, #dde2e7 45%, #ffffff 100%);
  }

  .net-volume {
    position: absolute; left: 0; right: 0; top: 1036px; text-align: center;
    font-family: 'Oswald', sans-serif; font-size: 18px; color: var(--ink); letter-spacing: 1px;
  }
</style>
</head>
<body>
<div class="canvas">
  <section class="box-front">
    <svg class="soft-curves" viewBox="0 0 285 1100" aria-hidden="true">
      <circle cx="230" cy="505" r="92" fill="#ffffff" opacity="0.85"/>
      <ellipse cx="40" cy="640" rx="150" ry="120" fill="#ffffff" opacity="0.7"/>
    </svg>

    <span class="brand-dot"></span>
    <div class="brand-name">Bloom<br>Froth</div>

    <h1 class="product-title">
      <span class="line-one">ALIGNER</span>
      <span class="line-two">CLEANER</span>
    </h1>

    <div class="supply-tag">30-DAY SUPPLY</div>

    <ul class="benefit-list">
      <li><svg viewBox="0 0 14 14"><path d="M2 7.5 L5.5 11 L12 3.5" fill="none" stroke="#1a5fc0" stroke-width="2.4"/></svg>Easy-to-use</li>
      <li><svg viewBox="0 0 14 14"><path d="M2 7.5 L5.5 11 L12 3.5" fill="none" stroke="#1a5fc0" stroke-width="2.4"/></svg>5-minute Cleaning</li>
      <li><svg viewBox="0 0 14 14"><path d="M2 7.5 L5.5 11 L12 3.5" fill="none" stroke="#1a5fc0" stroke-width="2.4"/></svg>Lasting Freshness</li>
      <li><svg viewBox="0 0 14 14"><path d="M2 7.5 L5.5 11 L12 3.5" fill="none" stroke="#1a5fc0" stroke-width="2.4"/></svg>Portable Design</li>
    </ul>

    <div class="flavor-badge">
      <svg viewBox="0 0 44 44" width="44" height="44" aria-hidden="true">
        <path d="M22 14 V30 M14 22 H30" stroke="#ffffff" stroke-width="5" stroke-linecap="round"/>
      </svg>
    </div>
    <div class="flavor-name">Mint Flavor</div>

    <div class="aligner-photo" role="img" aria-label="Photo of a clear dental aligner tray"></div>

    <div class="net-volume">50ml ℮ 1.69 Fl oz</div>
  </section>
</div>
</body>
</html>
```